Vistalune Web Design Project

We need a new web site for our company. Vistalune provides a range of location intelligence and marketing services to assist clients in improving their performance. On the location intelligence side we're the local partner for Orbix Terra (Charts and Globe) in South Africa, we're the local reseller and can assist company with the implementation and customization - we'll shortly receive the Orbix partner logo that should also be displayed on the Homepage. On the marketing side, we provide a range of marketing services for example Tenders, Event Management and Copy writing. The company is a blend between a mapping and marketing services company. You can have a look at the existing site at www.vistalune.co.za
Updates

Dear designers, the budget for my project has been increased to $700. Looking forward to receiving your designs. Kind regards Henrik

Dear designers - many thanks for all the great designs received to date. We'll provide feedback shortly. Kind regards Vistalune

Target Market(s)

Our target market is public and private organisations, and online customers (those with a web presence) primarily in South Africa

Industry/Entity Type

Marketing

Requirements
Must have
• I have uploaded the latest text and suggested pages at this stage. Important is that it should be easy to edit the pages in an HTML editor, e.g. Pagecraft. I suspect that the navigation will be expanded later e.g. careers, success stories - so it should be easy for me add new sections to the navigation later on. I have also uploaded the different Vistalune logo designs. Please include links on the Homepage for Terms and Conditions and PAIA - see www.vistalune.co.za - also the Copyright Note at the bottom of every page
Nice to have
• Although we're targeting corporates and government, and online customers, the site should be fresh and easy to navigate. I like the use of photographs on sites and make them look more interesting than simply text. Although we're also providing marketing services, the location intelligence (mapping) and Orbix Charts/Globe aspect are perhaps the most important part of the website.

```html
<!DOCTYPE html>
<html lang="en">
<head>
<meta charset="utf-8">
<title>Vistalune</title>
<link href="https://fonts.googleapis.com/css2?family=Arimo:wght@400;700&family=Open+Sans:wght@400;600&display=swap" rel="stylesheet">
<style>
:root{
  --page:#3b4047;
  --shell:#434a52;
  --stage:#383d43;
  --panel:#555d66;
  --panel-line:#6c747d;
  --nav:#3c4249;
  --red:#d51a1e;
  --white:#ffffff;
  --text:#e6e8ea;
  --dark:#2e3338;
}
*{margin:0;padding:0;box-sizing:border-box}
html,body{width:683px;height:1200px;overflow:hidden}
body{background:var(--page);font-family:"Arimo",Arial,sans-serif;color:var(--text);position:relative}
.abs{position:absolute}
.shell{position:absolute;left:37px;top:25px;width:608px;height:1108px;background:var(--shell);box-shadow:0 0 8px rgba(0,0,0,.45)}
.masthead{position:absolute;left:37px;top:25px;width:608px;height:72px;background:linear-gradient(#ffffff,#eceeef)}
.brand{position:absolute;left:28px;top:21px;display:flex;align-items:center;gap:6px;font:700 24px "Arimo",Arial,sans-serif;color:var(--red)}
.brand-dot{width:18px;height:18px;border-radius:50%;background:var(--dark)}
.phone{position:absolute;right:14px;top:25px;display:flex;align-items:center;gap:7px;font-size:13px;color:#333}
.phone-icon{width:20px;height:20px;border-radius:4px;background:var(--red);display:flex;align-items:center;justify-content:center}
.mainnav{position:absolute;left:37px;top:97px;width:608px;height:28px;background:var(--nav);display:flex;align-items:center;padding-left:37px;font-size:9.5px;color:var(--white)}
.mainnav a{color:var(--white);text-decoration:none;padding:5px 6px;border-radius:3px}
.mainnav .sep{margin:0 3px;color:#aab}
.mainnav .active{background:var(--red)}
.dropdown{position:absolute;left:191px;top:128px;width:118px;background:#3a4047;border-radius:0 0 4px 4px;padding:6px 0 5px;font-size:9px;z-index:3;box-shadow:0 2px 4px rgba(0,0,0,.4)}
.dropdown a{display:block;color:var(--white);text-decoration:none;padding:2px 14px;line-height:12px;white-space:nowrap}
.dropdown .current{background:var(--red)}
.stage{position:absolute;left:37px;top:125px;width:608px;height:233px;background:var(--stage)}
.slide{position:absolute;left:45px;top:130px;width:591px;height:220px;border:2px solid #f2f2f2;border-radius:6px;overflow:hidden;background:linear-gradient(120deg,#d9dde2 0%,#b8c6d4 35%,#7d8ea3 60%,#4b4f56 100%)}
.slide-caption{position:absolute;left:5px;top:151px;width:415px;padding:3px 6px;background:rgba(40,40,40,.72);font:400 13px/16px "Open Sans",sans-serif;color:var(--white)}
.arrow{position:absolute;top:100px;width:12px;height:12px;border-radius:50%;background:#fff;display:flex;align-items:center;justify-content:center}
h2{font:400 12px "Open Sans",sans-serif;color:var(--white);padding-bottom:3px;border-bottom:1px dotted #8a9199;display:inline-block}
h2 em{font-style:normal;color:var(--red)}
p{font-size:8.4px;line-height:14px;color:var(--text)}
.newsletter{position:absolute;left:468px;top:369px;width:165px;height:90px;border-radius:4px;background:linear-gradient(#ffffff,#d8d9da);padding:11px 13px}
.newsletter h3{font:400 9px "Arimo",sans-serif;color:#444;letter-spacing:.4px}
.newsletter .field{margin-top:10px;width:138px;height:16px;background:#454b52}
.newsletter .btn{margin:9px 0 0 22px;width:52px;height:24px;border-radius:3px;background:var(--red);color:#fff;font:700 7.5px/24px "Arimo",sans-serif;text-align:center}
.badge{position:absolute;left:563px;top:464px;width:67px;height:66px;border-radius:3px;background:linear-gradient(#ffffff 0,#ffffff 40%,#e3eef7 40%,#e3eef7 100%);border:1px solid #c9d3dc}
.features{position:absolute;left:55px;top:538px;width:580px;height:245px;background:var(--panel);border:1px solid var(--panel-line);border-radius:4px}
.feature{position:absolute;top:18px;width:180px}
.feature .pic{margin-top:4px;width:172px;height:92px;border-radius:3px}
.feature p{margin-top:8px;line-height:14px}
.divider{position:absolute;left:278px;top:24px;width:1px;height:210px;background:#7a828b}
.red{color:var(--red)}
.footer-links{position:absolute;right:52px;top:1152px;font-size:8.5px;color:var(--white);display:flex;gap:12px}
.copyright{position:absolute;left:451px;top:1174px;font-size:8.5px;color:var(--white)}
.social{position:absolute;left:48px;top:1157px;display:flex;gap:9px}
.social span{width:17px;height:17px;border-radius:50%}
</style>
</head>
<body>
<div class="shell"></div>

<header class="masthead">
  <div class="brand"><span class="brand-dot"></span>Vistalune</div>
  <div class="phone">
    <span class="phone-icon"><svg width="12" height="12" viewBox="0 0 24 24"><path fill="#fff" d="M6.6 10.8a15.2 15.2 0 0 0 6.6 6.6l2.2-2.2c.3-.3.7-.4 1-.2 1.1.4 2.3.6 3.6.6.6 0 1 .4 1 1V20c0 .6-.4 1-1 1A17 17 0 0 1 3 4c0-.6.4-1 1-1h3.5c.6 0 1 .4 1 1 0 1.3.2 2.5.6 3.6.1.3 0 .7-.2 1z"/></svg></span>
    +27 83 555 0192
  </div>
</header>

<nav class="mainnav">
  <a href="#">HOME</a><span class="sep"> </span>
  <a href="#">ABOUT US</a><span class="sep">|</span>
  <a href="#" class="active">SERVICES</a><span class="sep">|</span>
  <a href="#">PRODUCTS</a><span class="sep">|</span>
  <a href="#">CONTACT US</a>
</nav>
<div class="dropdown">
  <a href="#" class="current">Marketing Services</a>
  <a href="#">Consulting</a>
  <a href="#">Software Development</a>
</div>

<div class="stage"></div>
<div class="slide" role="img" aria-label="Business team in a meeting room with a bar chart on a screen">
  <span class="arrow" style="left:1px"><svg width="6" height="6" viewBox="0 0 6 6"><path d="M4 0L1 3l3 3z" fill="#333"/></svg></span>
  <span class="arrow" style="right:1px"><svg width="6" height="6" viewBox="0 0 6 6"><path d="M2 0l3 3-3 3z" fill="#333"/></svg></span>
  <div class="slide-caption">Vistalune provides a range of location intelligence and marketing services to assist clients in improving their performance</div>
</div>

<section class="abs" style="left:53px;top:368px;width:400px">
  <h2>Welcome to <em>Vistalune</em></h2>
  <p style="margin-top:4px">Vistalune provides a range of location intelligence and marketing services and products to assist clients in improving their performance. We enjoy challenging projects that stretch the imagination and encourage out of the box thinking. We have extensive experience in providing world-class service to private and public organisations, locally as well as internationally and we strive to build long-term lasting relationships with our clients.</p>
</section>

<aside class="newsletter">
  <h3>NEWSLETTER</h3>
  <div class="field"></div>
  <div class="btn">SUBSCRIBE</div>
</aside>
<div class="badge" role="img" aria-label="Authorised reseller badge"></div>

<section class="abs" style="left:56px;top:481px;width:450px">
  <h2>What makes us different?</h2>
  <p style="margin-top:4px;padding-left:2px">Our clients tell us that the experience working with Vistalune is distinctly different in a number of ways.</p>
</section>

<section class="features">
  <div class="feature" style="left:29px">
    <h2 style="border:0">Win-win</h2>
    <div class="pic" role="img" aria-label="Figures standing on a rising coloured bar chart with an arrow" style="background:linear-gradient(135deg,#ffffff 40%,#f1e36a 60%,#6ba6dd 80%,#e45050)"></div>
    <p>At Vistalune we follow a win-win approach to ensure that we provide value to our clients. Win-win means that we respect each other, that we are upfront about challenges and that we are passionate about improving of clients' business performance.</p>
  </div>
  <div class="divider"></div>
  <div class="feature" style="left:310px;width:252px">
    <h2 style="border:0">Expertise</h2>
    <div class="pic" role="img" aria-label="Hand holding a small tree against the sky" style="background:linear-gradient(#b9d3ec,#e8eef3 60%,#a08a6f)"></div>
    <p>The Vistalune team consists of experts with many years' experience, both in a technical and managerial capacity. Our associates are carefully selected and have a deep understanding of the industries we operate in. It is also a priority for us to stay abreast with the latest technologies and methodologies.</p>
  </div>
</section>

<section class="abs" style="left:59px;top:797px;width:560px">
  <h2>Broad-Based Black Economic Empowerment</h2>
  <p style="margin-top:6px">The Vistalune management accept that the legacy of apartheid excluded the majority of South Africans from ownership and/or control of productive assets and resources as well as severely restricting the acquisition of advanced skills and generally the effective participation in the economy. We support the Broad-Based Black Economic Empowerment (B-BBEE) initiatives of the South African Government aimed at promoting economic transformation in order to enable meaningful participation of black people in the economy.</p>
  <p style="margin-top:14px;width:520px">Vistalune complies with all relevant B-BBEE acts including Broad-Based Black Economic Empowerment Act 53 of 2003. Vistalune is a level 4 B-BBEE contributor.</p>
</section>

<section class="abs" style="left:60px;top:943px;width:565px">
  <h2>Why Vistalune?</h2>
  <p style="margin-top:6px">The name Vistalune was inspired by the book Meridian by Mara Vellin, A Tale of a Quiet Craftsman Who Answered the Hardest Navigation Question of His Era. During the great ages of exploration, <span class="red">"the longitude problem"</span> was the gravest of all scientific challenges. Lacking the ability to determine their longitude, sailors were literally lost at sea as soon as they lost sight of land. Ships ran aground on rocky shores; those traveling well-known routes were easy prey to pirates.</p>
  <p style="margin-top:14px">In 1714, England's Parliament offered a huge reward to anyone whose method of measuring longitude could be proven successful. The scientific establishment--from Aldo Ferrante to Sir Edwin Marlow--had mapped the heavens in its certainty of a celestial answer. In stark contrast, one man, Thomas Ardley, dared to imagine a mechanical solution--a clock that would keep precise time at sea, something no clock had been able to do on land. And the race was on....</p>
  <p style="margin-top:14px">At Vistalune it is also our goal to find innovative solutions for your business problems.</p>
</section>

<footer>
  <div class="social">
    <span style="background:#3b6cc4"></span>
    <span style="background:#3aa3dc"></span>
    <span style="background:#2c7bbf"></span>
    <span style="background:#e8761e"></span>
  </div>
  <div class="footer-links"><span>Privacy Policy</span><span>|</span><span>Terms &amp; Conditions</span><span>|</span><span>Contact Us</span></div>
  <div class="copyright">© 2012 Vistalune , All Rights Reserved</div>
</footer>
</body>
</html>
```